Hard-File Archival Services Billboard (Digitization Service) for Attorneys/Law Firms

I need a billboard design for my company "Velko Legal Aides" that advertises our primary service: Digitization of closed client files, for law firms and attorneys. Our system works as follows: 1) We get a call about a firm that wants to digitize their archived (closed) client files (which usually find their way to file cabinets or bankers boxes), 2) We go and pick those up from the law firm, 3) We bring them to our digitization facility, scan them in, and convert them into searchable PDF/A files, and 4) We upload them on the cloud, give the client a URL to visit their files whenever they want, and we delete them when requested by the client (usually for the retention duration for Missouri's rules of professional conduct, which is 6 years). It would be really cool to see "Velko Legal Aides" and the logo clearly on the billboard, some simple sentence relating to "Missouri's best digitizing and cloud storage service for closed client files for attorneys" (or something shorter, you get the point), with maybe a linear set of photos and arrows (as follows 1. A photo of a file cabinet opened with files hanging out of it, 2. an arrow pointing to a person scanning in documents in a big scanner (maybe with a Velko Legal Aidess logo on it?), 3. An arrow pointing to a "secure" appearing cloud (representing cloud storage), and 4. the client sitting at a computer with an arrow pointing back to the cloud (showing the client is accessing the cloud files through the computer). Our website is www.velkolegalaides.example if you want to glean any additional information from there. Thanks! Oh yes, I should also say the billboard dimensions (in the event you need this for photo aspect ratio) will be as follows: 14 feet tall by 48 feet wide.
Target Market(s)
Attorneys in Springfield, Missouri
Industry/Entity Type
Legal
Look and feel
Each slider illustrates characteristics of the customer's brand and the style your logo design should communicate.

```html
<!DOCTYPE html>
<html lang="en">
<head>
<meta charset="utf-8">
<title>Velko Legal Aides – Digitizing Billboard</title>
<link href="https://fonts.googleapis.com/css2?family=Montserrat:wght@600;700;800&display=swap" rel="stylesheet">
<style>
  :root {
    --ink: #111111;
    --charcoal: #2b2b2b;
    --paper: #ffffff;
    --backdrop: #e6e8eb;
    --ring: #f1f1f1;
    --rim-blue: #1f5fa8;
    --photo-light: #d9dce2;
    --photo-dark: #3a4666;
    --photo-mid: #8a8f99;
  }
  html, body {
    margin: 0;
    padding: 0;
    width: 1198px;
    height: 1200px;
    overflow: hidden;
    background: var(--backdrop);
    font-family: "Montserrat", Arial, sans-serif;
  }
  .billboard {
    position: absolute;
    left: 0;
    top: 426px;
    width: 1198px;
    height: 348px;
    background: var(--paper);
    overflow: hidden;
  }
  .wave, .photo-group { position: absolute; }
  .wave { left: 0; top: 0; }

  .brand {
    position: absolute;
    left: 40px;
    top: 130px;
    width: 275px;
    display: flex;
    align-items: center;
    gap: 14px;
  }
  .brand-mark {
    flex: none;
    width: 46px;
    height: 46px;
    border-radius: 50%;
    background: var(--ink);
  }
  .brand-name {
    margin: 0;
    font-weight: 800;
    font-size: 30px;
    line-height: 1.05;
    color: var(--ink);
    letter-spacing: 0.5px;
  }

  .message {
    position: absolute;
    left: 335px;
    top: 74px;
    width: 405px;
    color: var(--ink);
  }
  .message .lead {
    margin: 0;
    font-weight: 700;
    font-size: 51.5px;
    line-height: 54px;
    letter-spacing: -0.3px;
    white-space: nowrap;
  }
  .message .highlight {
    margin: 2px 0 0;
    background: var(--ink);
    color: var(--paper);
    font-weight: 700;
    font-size: 62px;
    line-height: 78px;
    height: 78px;
    text-align: center;
    letter-spacing: 0.5px;
  }
  .message .service {
    margin: 4px 0 0;
    font-weight: 700;
    font-size: 32px;
    line-height: 37px;
    white-space: nowrap;
  }
  .message .audience {
    margin: 0;
    font-weight: 700;
    font-size: 22.5px;
    line-height: 27px;
    white-space: nowrap;
  }
  .photo-group { left: 770px; top: 0; width: 428px; height: 348px; }
</style>
</head>
<body>
  <main class="billboard">
    <svg class="wave" width="450" height="125" viewBox="0 0 450 125" aria-hidden="true">
      <path d="M0 0 H440 C430 30 400 45 340 42 C280 40 230 30 180 55 C130 80 80 115 0 118 Z" fill="var(--charcoal)"/>
      <path d="M0 0 H300 C270 20 220 18 180 35 C130 55 90 95 0 100 Z" fill="var(--ink)"/>
    </svg>

    <div class="brand">
      <span class="brand-mark"></span>
      <p class="brand-name">Velko<br>Legal Aides</p>
    </div>

    <section class="message">
      <h1 class="lead">Missouri's best</h1>
      <p class="highlight">DIGITIZING</p>
      <p class="service">&amp; cloud storage service</p>
      <p class="audience">for closed client files for attorneys</p>
    </section>

    <svg class="photo-group" width="428" height="348" viewBox="0 0 428 348">
      <defs>
        <linearGradient id="shelfTones" x1="0" y1="0" x2="1" y2="1">
          <stop offset="0" stop-color="var(--photo-light)"/>
          <stop offset="0.5" stop-color="var(--photo-dark)"/>
          <stop offset="1" stop-color="var(--photo-light)"/>
        </linearGradient>
        <radialGradient id="cloudTones" cx="0.45" cy="0.4" r="0.7">
          <stop offset="0" stop-color="#c9ccd1"/>
          <stop offset="1" stop-color="var(--photo-mid)"/>
        </radialGradient>
      </defs>
      <circle cx="247" cy="174" r="180" fill="var(--ring)"/>
      <circle cx="247" cy="174" r="149" fill="url(#shelfTones)" role="img" aria-label="Photo of a hand pulling a binder from a shelf of office file folders"/>
      <circle cx="92" cy="254" r="90" fill="var(--rim-blue)"/>
      <circle cx="89" cy="252" r="86" fill="url(#cloudTones)" role="img" aria-label="Photo of hands typing on a laptop beneath a digital cloud storage graphic"/>
    </svg>
  </main>
</body>
</html>
```